Fully Functional Wix Website, Not Just Images

Please read all instructions carefully. This is NOT merely a design project where the artist will deliver static images. This project requires that the designer build a fully functional SEO optimized website within Wix then transfer full ownership to me. See attached "instructions for design" file. I have wix for other websites. Only wix is acceptable. Do not submit more than 1 design per designer. If you submit more than 1 design I will award to someone else.

Target Market(s)

see attachments and brisvale482.com

Industry/Entity Type

Coding

Coded - Design and coding required

Number of Pages Required

4 page

Font styles to use
Other font styles liked:
• see attachments and brisvale482.com

Requirements
Must have
Nice to have
Should not have

```html
<!DOCTYPE html>
<html lang="en">
<head>
<meta charset="utf-8">
<title>Brisvale482 Press — The Complete Monograph Collection</title>
<link href="https://fonts.googleapis.com/css2?family=Playfair+Display:wght@400;500;600&family=DM+Sans:wght@400;500;600;700&display=swap" rel="stylesheet">
<style>
:root{
  --ink:#111214;
  --muted:#5b5d61;
  --soft:#8a8c90;
  --rust:#b4481f;
  --cream:#f7f5f0;
  --stone:#efede8;
  --panel:#f1efea;
  --white:#ffffff;
  --navy:#14203a;
  --navy-card:#1a2948;
  --rule:#e3e0d9;
  --serif:'Playfair Display', Georgia, serif;
  --sans:'DM Sans', Helvetica, Arial, sans-serif;
}
*{margin:0;padding:0;box-sizing:border-box}
html,body{width:1200px;height:4942px;overflow:hidden}
body{font-family:var(--sans);color:var(--ink);background:var(--white);position:relative}
.abs{position:absolute}
section,header,footer{position:absolute;left:0;width:1200px}

/* nav */
.site-nav{top:0;height:77px;background:var(--cream);border-bottom:1px solid var(--rule)}
.brand{font-family:var(--serif);font-weight:600;font-size:19px;letter-spacing:.5px;color:var(--ink)}
.nav-link{font-size:11px;letter-spacing:1.4px;color:var(--muted);text-transform:uppercase;font-weight:500}
.nav-link.active{color:var(--ink);font-weight:700}
.nav-cta{left:847px;top:15px;width:186px;height:46px;background:var(--ink);color:#fff;font-size:10px;letter-spacing:1.5px;font-weight:600;padding:12px 26px;line-height:1.25}
.avatar{left:1060px;top:22px;width:32px;height:32px;border-radius:50%;background:radial-gradient(circle at 45% 40%,#b89a82,#5b4a3e)}

/* shared */
.eyebrow{font-size:10px;letter-spacing:1.8px;text-transform:uppercase;color:var(--rust);font-weight:600}
.title{font-family:var(--serif);font-weight:600;color:var(--ink);font-size:38px;line-height:45px}
.byline{font-size:11px;letter-spacing:1px;text-transform:uppercase;color:var(--muted);font-weight:500}
.body-copy{font-size:13.5px;line-height:24px;color:#4a4c50}
.spec{padding:22px 22px;background:var(--panel)}
.spec-row{display:flex;justify-content:space-between;align-items:flex-start;height:32px;font-size:12px;color:var(--ink)}
.spec-row .k{font-size:9px;letter-spacing:1.2px;color:var(--soft);text-transform:uppercase;padding-top:2px;width:96px}
.spec-row .v{text-align:right;flex:1}
.spec-row .v.isbn{color:var(--rust)}
.price{display:flex;align-items:flex-start;gap:8px}
.price .amt{font-family:var(--serif);font-size:36px;line-height:40px;font-weight:500}
.price .unit{font-size:9px;letter-spacing:1px;color:var(--muted);text-transform:uppercase;line-height:11px;padding-top:14px;width:64px}
.price .status{font-size:9.5px;letter-spacing:1.3px;color:var(--rust);text-transform:uppercase;line-height:11px;padding-top:14px;width:180px;font-weight:600}
.btn{position:absolute;height:69px;display:flex;align-items:center;justify-content:center;text-align:center;font-size:10px;letter-spacing:1.5px;font-weight:700;text-transform:uppercase;line-height:13px}
.btn.primary{background:var(--ink);color:#fff}
.btn.secondary{background:var(--stone);color:var(--ink)}
.plate-caption{font-size:9.5px;letter-spacing:1.2px;color:var(--muted);text-transform:uppercase;display:flex;justify-content:space-between}

/* hero */
.hero{top:77px;height:749px;background:var(--cream)}
.hero-title{font-family:var(--serif);font-weight:400;font-size:64px;line-height:71px;color:var(--ink)}
.stats{left:111px;top:489px;width:976px;height:148px;background:var(--stone);display:flex;padding:32px 31px}
.stat{width:233px}
.stat .k{font-size:9.5px;letter-spacing:1.5px;color:var(--muted);text-transform:uppercase;font-weight:600}
.stat .n{font-family:var(--serif);font-size:38px;line-height:46px;margin-top:4px}
.stat .n.rust{color:var(--rust)}
.stat .d{font-size:12px;color:var(--muted)}

/* volume sections */
.vol-one{top:826px;height:973px;background:var(--white)}
.vol-two{top:1799px;height:995px;background:var(--stone)}
.vol-three{top:2794px;height:988px;background:var(--white)}

/* trilogy */
.trilogy{top:3782px;height:768px;background:var(--navy);color:#fff}
.trilogy .eyebrow{color:#d2a58f}
.trilogy-title{font-family:var(--serif);font-size:56px;line-height:60px;font-weight:400}
.trilogy-copy{font-size:14px;line-height:27px;color:#aeb6c6}
.feature{background:var(--navy-card);padding:18px 16px;width:173px;height:111px}
.feature .k{font-size:9.5px;letter-spacing:1.3px;color:#fff;font-weight:700}
.feature .v{font-size:12px;line-height:25px;color:#d7dce6;margin-top:2px}
.set-card{left:697px;top:112px;width:390px;height:541px;background:#fbf9f3;color:var(--ink);padding:42px 46px}
.set-list li{list-style:none;display:flex;gap:10px;font-size:12px;line-height:19px;color:#4a4c50;margin-bottom:12px}
.set-list svg{flex:none;margin-top:4px}

/* footer */
.site-footer{top:4550px;height:392px;background:#f4f2ed}
.foot-head{font-size:9.5px;letter-spacing:1.2px;font-weight:700;text-transform:uppercase;line-height:13px}
.foot-links{font-size:12px;line-height:19px;color:var(--muted);margin-top:10px}
.foot-links div{margin-bottom:10px}
.legal{font-size:10px;letter-spacing:1.2px;color:var(--muted);text-transform:uppercase}
</style>
</head>
<body>

<header class="site-nav">
  <div class="abs brand" style="left:357px;top:26px">BRISVALE482</div>
  <div class="abs nav-link" style="left:478px;top:30px">Home</div>
  <div class="abs nav-link active" style="left:547px;top:30px">Books</div>
  <div class="abs nav-link" style="left:634px;top:30px">About</div>
  <div class="abs nav-link" style="left:708px;top:23px;line-height:13px">Gallery &amp;<br>Contact</div>
  <div class="abs nav-cta">Acquire the<br>series</div>
  <div class="abs avatar" role="img" aria-label="Patron account portrait"></div>
</header>

<section class="hero">
  <div class="abs eyebrow" style="left:111px;top:109px;display:flex;align-items:center;gap:12px"><span style="width:30px;height:1px;background:var(--rust);display:block"></span>The Complete Monograph Collection</div>
  <h1 class="abs hero-title" style="left:111px;top:148px;width:640px">Three Definitive Treatises on Seamanship, Wind &amp; Harbor Command.</h1>
  <p class="abs body-copy" style="left:781px;top:226px;width:310px">Crafted across five decades of commercial navigation, each volume pairs rigorous hydrographic analysis with uncompromising letterpress bookbinding. Hand-bound in archival buckram cloth with hot-stamped metallic foil and gatefold navigation plates on 140gsm Alder Pure stock.</p>
  <div class="abs stats">
    <div class="stat"><div class="k">Volumes</div><div class="n">03</div><div class="d">Complete master folio</div></div>
    <div class="stat"><div class="k">Pagination</div><div class="n">840</div><div class="d">Archival text &amp; charts</div></div>
    <div class="stat"><div class="k">Illustrations</div><div class="n">260</div><div class="d">Vector hydrodynamic schematics</div></div>
    <div class="stat"><div class="k">Construction</div><div class="n rust">Pure</div><div class="d">Hand-bound hardcovers</div></div>
  </div>
</section>

<section class="vol-one">
  <div class="abs" style="left:96px;top:393px;width:576px;height:192px;background:#ecebe6;transform:rotate(-.6deg)"></div>
  <div class="abs" style="left:104px;top:399px;width:562px;height:178px;background:#f5f4f0;box-shadow:0 10px 24px rgba(0,0,0,.08);padding:0 44px">
    <div class="plate-caption" style="position:absolute;left:44px;right:44px;bottom:38px"><span>Plate Folio: Edition 1.4</span><span>Coordinates: 41°31′ N, 71°19′ W</span></div>
  </div>
  <div class="abs eyebrow" style="left:714px;top:114px;font-size:9px">Volume I • Core Seamanship</div>
  <h2 class="abs title" style="left:714px;top:142px;width:373px">The Art of Docking: Precision, Wind &amp; Current</h2>
  <div class="abs byline" style="left:714px;top:282px">By Captain Rowan Mercer</div>
  <p class="abs body-copy" style="left:714px;top:318px;width:373px">A definitive study on hydrodynamic behavior in confined waters. Mercer deconstructs vector slip approaches, pivot point migration during deceleration, and spring line tension control under opposing gale tides. Illustrated with ninety-two fold-out tidal vector diagrams engineered for single-handed and crewed maneuvers.</p>
  <div class="abs spec" style="left:714px;top:512px;width:373px;height:154px">
    <div class="spec-row"><span class="k">Binding</span><span class="v">Quarter-bound cloth &amp; navy leatherette</span></div>
    <div class="spec-row"><span class="k">Embossing</span><span class="v">Triple-strike 22k gold leaf foil</span></div>
    <div class="spec-row"><span class="k">Extent &amp; Paper</span><span class="v">288 Pages · 140gsm Alder Pure</span></div>
    <div class="spec-row"><span class="k">Archival Index</span><span class="v isbn">ISBN 978-0-98831-01-2</span></div>
  </div>
  <div class="abs price" style="left:714px;top:712px"><span class="amt">$145.00</span><span class="unit">USD / First Edition</span><span class="status">Available for immediate dispatch</span></div>
  <div class="btn primary" style="left:714px;top:793px;width:154px">Acquire<br>Hardcover<br>Edition</div>
  <div class="btn secondary" style="left:885px;top:793px;width:202px">Sample Chapter (PDF) →</div>
</section>

<section class="vol-two">
  <div class="abs eyebrow" style="left:111px;top:119px;font-size:9px">Volume II • Crisis &amp; Heavy Weather</div>
  <h2 class="abs title" style="left:111px;top:144px;width:380px">Calm in the Tempest: Heavy Weather Seamanship &amp; Crisis Management</h2>
  <div class="abs byline" style="left:111px;top:326px">By Captain Tobias H. Wren</div>
  <p class="abs body-copy" style="left:111px;top:360px;width:375px">Wren’s monumental manual examines the breaking point between hull physics and psychology in force 10 conditions. Includes rigorous mathematical modeling on righting moments under confused seas, drogue deployment matrices, rudder pressure relief protocols, and emergency grounding avoidance.</p>
  <div class="abs spec" style="left:111px;top:532px;width:375px;height:161px;background:var(--white)">
    <div class="spec-row"><span class="k">Binding</span><span class="v">Terracotta book-buckram cloth</span></div>
    <div class="spec-row"><span class="k">Foil Work</span><span class="v">High-relief tempest crest &amp; wave foil</span></div>
    <div class="spec-row"><span class="k">Extent &amp; Paper</span><span class="v">320 Pages · Gilt edge archival cream</span></div>
    <div class="spec-row"><span class="k">Archival Index</span><span class="v isbn">ISBN 978-0-98831-02-9</span></div>
  </div>
  <div class="abs price" style="left:111px;top:734px"><span class="amt">$165.00</span><span class="unit">USD / Archival Cloth</span><span class="status">Limited print run (500 copies)</span></div>
  <div class="btn primary" style="left:111px;top:812px;width:157px">Acquire<br>Hardcover<br>Edition</div>
  <div class="btn secondary" style="left:285px;top:812px;width:201px">Sample Chapter (PDF) →</div>

  <div class="abs" style="left:530px;top:188px;width:578px;height:618px;background:#e8ded4"></div>
  <div class="abs" style="left:543px;top:207px;width:542px;height:582px;background:var(--white);box-shadow:0 12px 30px rgba(0,0,0,.1)">
    <div class="abs" role="img" aria-label="Portrait of a weathered sea captain seated on a marina dock at golden hour" style="left:35px;top:39px;width:472px;height:470px;background:linear-gradient(160deg,#d8b88a 0%,#8f8a80 40%,#2e3440 75%,#1c2230 100%)"></div>
    <div class="plate-caption abs" style="left:35px;width:472px;top:532px;font-size:9px"><span>Gale Scale: Beaufort 8–12</span><span>Oceanic Sea Station: 58°N North Atlantic</span></div>
  </div>
</section>

<section class="vol-three">
  <div class="abs" style="left:90px;top:105px;width:576px;height:778px;background:#dfe4ea;transform:rotate(-1deg)"></div>
  <div class="abs" style="left:111px;top:119px;width:546px;height:745px;background:var(--white);box-shadow:0 12px 30px rgba(0,0,0,.08)">
    <div class="abs" role="img" aria-label="Olive linen hardcover of Harbor Masteries resting on a desk beside a brass lamp and marina window" style="left:39px;top:44px;width:470px;height:628px;background:linear-gradient(170deg,#c9c5bb 0%,#6e5a47 35%,#3c3f2e 60%,#4a2b1d 100%)"></div>
    <div class="plate-caption abs" style="left:39px;width:470px;top:702px;font-size:9px"><span>Close Marina Tactics</span><span>Berth Precision: ± 2 Inches</span></div>
  </div>
  <div class="abs eyebrow" style="left:714px;top:114px;font-size:9px">Volume III • Close-Quarters Maneuvering</div>
  <h2 class="abs title" style="left:714px;top:140px;width:380px">Harbor Masteries: Close-Quarters Yacht Handling</h2>
  <div class="abs byline" style="left:714px;top:282px">By Captain Rowan Mercer &amp; Senior Pilots</div>
  <p class="abs body-copy" style="left:714px;top:316px;width:373px">Written in collaboration with Mediterranean and Puget Sound docking masters, this volume demystifies high-windage hull control, bow thruster battery thermal cycles, and tight-radius propeller walk utilization in high-density marinas. Features sixty step-by-step overhead docking diagrams.</p>
  <div class="abs spec" style="left:714px;top:489px;width:373px;height:211px">
    <div class="spec-row" style="height:34px"><span class="k">Binding</span><span class="v">Dark olive linen cloth hardbound</span></div>
    <div class="spec-row" style="height:56px"><span class="k">Embossing</span><span class="v" style="text-align:left">Hand-pressed brass helm &amp; mooring cleat</span></div>
    <div class="spec-row" style="height:52px"><span class="k">Extent &amp; Paper</span><span class="v" style="text-align:left">232 Pages · Heavy matte archival stock</span></div>
    <div class="spec-row"><span class="k">Archival Index</span><span class="v isbn">ISBN 978-0-98831-03-6</span></div>
  </div>
  <div class="abs price" style="left:714px;top:738px"><span class="amt">$135.00</span><span class="unit">USD / First Edition</span><span class="status">Available for immediate dispatch</span></div>
  <div class="btn primary" style="left:714px;top:808px;width:154px">Acquire<br>Hardcover<br>Edition</div>
  <div class="btn secondary" style="left:885px;top:808px;width:202px">Sample Chapter (PDF) →</div>
</section>

<section class="trilogy">
  <div class="abs eyebrow" style="left:111px;top:130px;display:flex;align-items:center;gap:12px;font-size:9px"><span style="width:30px;height:1px;background:#d2a58f;display:block"></span>Limited Archival Release • 250 Signed Sets</div>
  <h2 class="abs trilogy-title" style="left:111px;top:164px;width:560px">The Captain’s Slipcase Trilogy</h2>
  <p class="abs trilogy-copy" style="left:111px;top:330px;width:555px">All three volumes presented in a hand-crafted American black walnut slipcase, completed with an individually numbered solid brass commissioning plaque. Each trilogy includes a set of weighted solid brass navigation dividers, two milled chart weights, and an embossed certificate signed by Captain Mercer and Captain Wren.</p>
  <div class="abs feature" style="left:111px;top:490px"><div class="k">ENCLOSURE</div><div class="v">Walnut slipcase with brass inlay</div></div>
  <div class="abs feature" style="left:301px;top:490px"><div class="k">INSTRUMENTS</div><div class="v">Milled brass divider &amp; chart weights</div></div>
  <div class="abs feature" style="left:493px;top:490px"><div class="k">PROVENANCE</div><div class="v">Signed &amp; registry-numbered certificate</div></div>

  <div class="abs set-card">
    <div style="display:flex;gap:36px;font-size:9.5px;letter-spacing:1.2px;font-weight:600"><span style="color:var(--rust)">TRILOGY BOX SET</span><span style="color:var(--muted)">FREE INSURED COURIER</span></div>
    <div style="display:flex;align-items:flex-end;gap:12px;margin-top:28px"><span style="font-family:var(--serif);font-size:48px;line-height:50px">$395.00</span><span style="font-size:9px;letter-spacing:1px;color:var(--muted);padding-bottom:6px">USD COMPLETE</span></div>
    <div style="font-size:12px;line-height:20px;color:var(--rust);margin-top:6px;width:260px">Save $50 compared to individual edition acquisition.</div>
    <ul class="set-list" style="margin-top:30px">
      <li><svg width="10" height="8" viewBox="0 0 10 8"><path d="M1 4l3 3 5-6" fill="none" stroke="#b4481f" stroke-width="1.4"/></svg>Volume I: The Art of Docking (Navy &amp; Gold)</li>
      <li><svg width="10" height="8" viewBox="0 0 10 8"><path d="M1 4l3 3 5-6" fill="none" stroke="#b4481f" stroke-width="1.4"/></svg>Volume II: Calm in the Tempest (Terracotta Cloth)</li>
      <li><svg width="10" height="8" viewBox="0 0 10 8"><path d="M1 4l3 3 5-6" fill="none" stroke="#b4481f" stroke-width="1.4"/></svg>Volume III: Harbor Masteries (Olive Linen)</li>
      <li><svg width="10" height="8" viewBox="0 0 10 8"><path d="M1 4l3 3 5-6" fill="none" stroke="#b4481f" stroke-width="1.4"/></svg>Solid brass numbered registry plaque</li>
    </ul>
    <div style="margin-top:22px;height:50px;background:var(--ink);color:#fff;display:flex;align-items:center;justify-content:center;font-size:10.5px;letter-spacing:1.5px;font-weight:700">ORDER COMPLETE TRILOGY BOX SET</div>
    <div style="margin-top:16px;text-align:center;font-size:9px;letter-spacing:1.2px;color:var(--muted);line-height:13px;padding:0 20px">DISPATCHED WITHIN 24 HOURS IN MUSEUM-GRADE PACKAGING.</div>
  </div>
</section>

<footer class="site-footer">
  <div class="abs brand" style="left:298px;top:66px;font-size:18px">BRISVALE482</div>
  <div class="abs" style="left:111px;top:96px;width:320px;font-size:12px;line-height:20px;color:var(--muted)">Maritime &amp; Literary Press — Master Class Seamanship, Literature &amp; Harbor Command.</div>
  <div class="abs eyebrow" style="left:111px;top:152px;font-size:9.5px">Archival Volume III · Est. 2024</div>

  <div class="abs" style="left:447px;top:56px;width:90px"><div class="foot-head">The Editions</div><div class="foot-links"><div>Volume I</div><div>Volume II</div><div>Collector Folio</div><div>Field Guides</div></div></div>
  <div class="abs" style="left:547px;top:56px;width:92px"><div class="foot-head">The Press</div><div class="foot-links"><div>Monograph</div><div>Philosophy</div><div>Patrons</div><div>Curator Notes</div></div></div>
  <div class="abs" style="left:649px;top:56px;width:92px"><div class="foot-head">Monograph Archive</div><div class="foot-links"><div>Plates &amp; Charts</div><div>Nautical Blueprints</div><div>Harbor Logs</div><div>Visual Gallery</div></div></div>
  <div class="abs" style="left:749px;top:56px;width:92px"><div class="foot-head">Inquiries</div><div class="foot-links"><div>Press &amp; Media</div><div>Harbor Master</div><div>Acquisitions</div><div>Bespoke Folios</div></div></div>
  <div class="abs" style="left:864px;top:56px;width:223px">
    <div class="foot-head">The Harbor Dispatch</div>
    <div style="font-size:12px;line-height:20px;color:var(--muted);margin-top:8px">Weekly seamanship notes &amp; private release briefings.</div>
    <div style="margin-top:16px;border-bottom:1px solid #9a9a98;display:flex;justify-content:space-between;padding-bottom:8px;font-size:11px;color:#a9a9a6"><span>Enter patron email address</span><svg width="14" height="10" viewBox="0 0 14 10"><path d="M0 5h12M8 1l4 4-4 4" fill="none" stroke="#111214" stroke-width="1.3"/></svg></div>
    <div style="font-size:9px;letter-spacing:1px;color:var(--soft);margin-top:10px;line-height:12px">Strictly reserved for archival subscribers.</div>
  </div>

  <div class="abs" style="left:111px;top:326px;width:300px;font-size:11px;line-height:20px;color:var(--muted)">Copyright © 2025 Brisvale482 Press. All rights reserved.</div>
  <div class="abs legal" style="left:490px;top:326px;display:flex;gap:34px"><span>Privacy Policy</span><span>Terms of Service</span><span>Shipping &amp; Monograph Dispatch</span></div>
  <div class="abs legal" style="left:676px;top:352px">Accessibility Statement</div>
</footer>

</body>
</html>
```